Business card design for Velvet Harbor

We need business cards designed for our new marketing consulting company, Velvet Harbor. Our services include marketing strategy, go-to-market and launch planning, growth strategy, and execution. We serve medical technology and health technology companies, from startups to well-established growth companies.

The business cards should feel professional, credible, reliable and trustworthy, and should instill confidence. Also bold, creative, and modern.

The design must use the Velvet Harbor logo.

The primary brand color is this orange: #FF5501
A secondary color that you can use is this gray: #282B2D
I would prefer only to use the orange and gray. But if you feel you really need an additional accent color (please use it very sparingly, as little as possible), you can use this blue for small accent purposes: #009FED

Attached are the logo files. The main logo is the one with a little bit of orange on the left and the rest is gray.

The business card should include the following:

Velvet Harbor logo
First name and last name
Title
Email address
Phone number and type (in whatever order looks best for the design
Website (the website does not need to be in the same block as the personal info)

For example:

Nessa Pryle
Founder & Principal
nessa@velvetharbor.com
+1.628.309.4156 mobile (can use "." or spaces in between blocks of numbers)
velvetharbor.com (somewhere on the card, it does not need to be with the personal info; and note that there is no "www." at the beginning)

Note that there will be no address listed on the business card.

Target Market(s)

Executives (CEO, head of marketing, head of sales) at medical technology and health technology companies, mostly in their 40s and older, well-educated, often with advanced degrees. They are strategic thinkers, responsible for budgets, and familiar with P&L. Their comfort with and trust in using outside consultants varies.

Industry/Entity Type

Medical technology and health technology companies.

Contact Information for Business Card

See project description

Font styles to use
Sans Serif

Requirements
Must have
• Logo and see Business card details section above.

```html
<!DOCTYPE html>
<html lang="en">
<head>
<meta charset="utf-8">
<title>Velvet Harbor – Business Card</title>
<link rel="stylesheet" href="https://fonts.googleapis.com/css2?family=Michroma&family=Arimo:wght@400;500&display=swap">
<style>
  :root {
    --backdrop: #3e3e3e;
    --paper: #ffffff;
    --charcoal: #282b2d;
    --orange: #ff5501;
    --ink: #2b2e30;
    --emboss: #6a6f73;
  }
  * { box-sizing: border-box; margin: 0; padding: 0; }
  html, body { width: 1200px; height: 803px; overflow: hidden; }
  body {
    background: var(--backdrop);
    position: relative;
    font-family: "Arimo", Arial, sans-serif;
  }
  .card {
    position: absolute;
    top: 252px;
    width: 525px;
    height: 300px;
    border-radius: 22px;
    border-bottom: 3px solid var(--orange);
    overflow: hidden;
  }
  .card--front { left: 50px; background: var(--paper); }
  .card--back  { left: 625px; background: var(--charcoal); border-right: 2px solid var(--orange); }

  .logotype {
    font-family: "Michroma", "Arial Black", sans-serif;
    text-transform: uppercase;
    line-height: 1.15;
  }
  .card--front .logo-lockup {
    position: absolute;
    left: 36px; top: 38px;
    display: flex; align-items: center; gap: 16px;
  }
  .card--front .mark-circle {
    width: 40px; height: 40px; border-radius: 50%;
    background: var(--orange);
    flex: none;
  }
  .card--front .logotype {
    font-size: 22px;
    letter-spacing: 6px;
    color: var(--ink);
  }
  .person {
    position: absolute;
    left: 36px; top: 140px;
  }
  .person__name {
    font-family: "Michroma", sans-serif;
    font-size: 18px;
    color: var(--orange);
  }
  .person__title {
    font-size: 12px;
    color: var(--ink);
    margin-top: 3px;
  }
  .contacts {
    list-style: none;
    margin-top: 16px;
    font-size: 12px;
    line-height: 1.6;
    color: var(--ink);
  }
  .contacts li { display: flex; align-items: center; gap: 7px; }
  .contacts svg { width: 10px; height: 10px; fill: none; stroke: var(--orange); stroke-width: 1.6; }
  .contacts .type { color: var(--emboss); }

  .card--back .logo-lockup {
    position: absolute;
    left: 50%; top: 50%;
    transform: translate(-50%, -50%);
    display: flex; align-items: center; gap: 26px;
  }
  .card--back .mark-circle {
    width: 58px; height: 58px; border-radius: 50%;
    background: var(--emboss);
    flex: none;
  }
  .card--back .logotype {
    font-size: 24px;
    letter-spacing: 7px;
    color: var(--emboss);
  }
</style>
</head>
<body>
  <section class="card card--front" aria-label="Business card front">
    <div class="logo-lockup">
      <div class="mark-circle"></div>
      <div class="logotype">Velvet<br>Harbor</div>
    </div>
    <div class="person">
      <div class="person__name">Nessa Pryle</div>
      <div class="person__title">President</div>
      <ul class="contacts">
        <li><svg viewBox="0 0 10 10"><rect x="2.5" y="0.8" width="5" height="8.4" rx="1"/></svg>+1.628.309.4156 <span class="type">mobile</span></li>
        <li><svg viewBox="0 0 10 10"><rect x="0.8" y="2" width="8.4" height="6"/><path d="M0.8 2 L5 5.5 L9.2 2"/></svg>nessa@velvetharbor.com</li>
        <li><svg viewBox="0 0 10 10"><circle cx="5" cy="5" r="4.2"/><path d="M0.8 5 H9.2 M5 0.8 Q2.5 5 5 9.2 Q7.5 5 5 0.8"/></svg>velvetharbor.com</li>
      </ul>
    </div>
  </section>

  <section class="card card--back" aria-label="Business card back">
    <div class="logo-lockup">
      <div class="mark-circle"></div>
      <div class="logotype">Velvet<br>Harbor</div>
    </div>
  </section>
</body>
</html>
```